The Timber Loft

We need a business card design for our wardrobe company.
Please visit our website www.zorvelcabinets.com to get an idea of who we are.

```html
<!DOCTYPE html>
<html lang="en">
<head>
<meta charset="utf-8">
<title>The Timber Loft – Business Card</title>
<link href="https://fonts.googleapis.com/css2?family=Mulish:wght@400;600;700;800&display=swap" rel="stylesheet">
<style>
  :root {
    --backdrop: #dcdddf;
    --card-dark: #231f20;
    --card-light: #ffffff;
    --ink: #231f20;
    --ink-soft: #2b2b2b;
    --on-dark: #ffffff;
  }
  * { margin: 0; padding: 0; box-sizing: border-box; }
  html, body {
    width: 1164px; height: 1200px; overflow: hidden;
    background: var(--backdrop);
    font-family: "Mulish", Arial, sans-serif;
  }
  .canvas { position: relative; width: 1164px; height: 1200px; }
  .card {
    position: absolute; left: 227px; width: 710px; height: 458px;
    box-shadow: 0 0 26px rgba(0,0,0,0.12);
  }
  .card--front { top: 114px; background: var(--card-dark); }
  .card--back { top: 629px; background: var(--card-light); color: var(--ink); }

  .brand-mark {
    position: absolute; left: 216px; top: 201px;
    width: 58px; height: 58px; background: var(--on-dark);
  }
  .brand-text {
    position: absolute; left: 298px; top: 196px;
    color: var(--on-dark); font-weight: 700; white-space: nowrap;
  }
  .brand-name { font-size: 25px; letter-spacing: 0.2px; line-height: 32px; }
  .brand-tagline { font-size: 20px; line-height: 30px; margin-left: 28px; margin-top: 4px; }

  .back-brand {
    position: absolute; left: 33px; top: 66px;
    font-size: 26px; font-weight: 700; color: var(--ink); white-space: nowrap;
  }

  .person {
    position: absolute; right: 28px; top: 232px; text-align: right; white-space: nowrap;
  }
  .person-name { font-size: 26px; font-weight: 800; letter-spacing: 0.6px; line-height: 30px; }
  .person-role { font-size: 19px; font-weight: 400; line-height: 26px; margin-top: 2px; color: var(--ink-soft); }

  .contact-list {
    position: absolute; right: 28px; top: 324px; list-style: none;
  }
  .contact-item {
    display: flex; justify-content: flex-end; align-items: center;
    height: 28.5px; font-size: 19px; color: var(--ink-soft); white-space: nowrap;
  }
  .contact-icon { width: 18px; height: 18px; margin-left: 9px; fill: var(--ink); flex: none; }
</style>
</head>
<body>
<main class="canvas">
  <section class="card card--front" aria-label="Business card front">
    <div class="brand-mark"></div>
    <div class="brand-text">
      <div class="brand-name">THE TIMBER LOFT</div>
      <div class="brand-tagline">Built to Fit Every Room</div>
    </div>
  </section>

  <section class="card card--back" aria-label="Business card back">
    <div class="back-brand">The Timber Loft</div>

    <div class="person">
      <div class="person-name">MAREN HOLST</div>
      <div class="person-role">Design Consultant &amp; Dream Maker</div>
    </div>

    <ul class="contact-list">
      <li class="contact-item">0207 555 0148
        <svg class="contact-icon" viewBox="0 0 24 24" aria-hidden="true"><path d="M6.6 10.8a15.1 15.1 0 0 0 6.6 6.6l2.2-2.2c.3-.3.7-.4 1-.2 1.1.4 2.3.6 3.6.6.6 0 1 .4 1 1V20c0 .6-.4 1-1 1A17 17 0 0 1 3 4c0-.6.4-1 1-1h3.5c.6 0 1 .4 1 1 0 1.3.2 2.5.6 3.6.1.3 0 .7-.2 1z"/></svg>
      </li>
      <li class="contact-item">maren@zorvelcabinets.com
        <svg class="contact-icon" viewBox="0 0 24 24" aria-hidden="true"><path d="M2 4h20v16H2z"/><path d="M3 5.5l9 6.5 9-6.5" fill="none" stroke="#fff" stroke-width="1.6"/></svg>
      </li>
      <li class="contact-item">www.zorvelcabinets.com
        <svg class="contact-icon" viewBox="0 0 24 24" aria-hidden="true"><path d="M12 2a10 10 0 1 0 0 20 10 10 0 0 0 0-20zm6.9 6h-2.8a15 15 0 0 0-1.3-3.6A8 8 0 0 1 18.9 8zM12 4c.8 1.1 1.5 2.5 1.9 4h-3.8c.4-1.5 1.1-2.9 1.9-4zM4.3 14a8 8 0 0 1 0-4h3.2a16 16 0 0 0 0 4zm.8 2h2.8c.3 1.3.8 2.5 1.3 3.6A8 8 0 0 1 5.1 16zm2.8-8H5.1a8 8 0 0 1 4.1-3.6C8.7 5.5 8.2 6.7 7.9 8zM12 20c-.8-1.1-1.5-2.5-1.9-4h3.8c-.4 1.5-1.1 2.9-1.9 4zm2.3-6H9.7a14 14 0 0 1 0-4h4.6a14 14 0 0 1 0 4zm.5 5.6c.5-1.1 1-2.3 1.3-3.6h2.8a8 8 0 0 1-4.1 3.6zM16.5 14a16 16 0 0 0 0-4h3.2a8 8 0 0 1 0 4z"/></svg>
      </li>
      <li class="contact-item">Larch Yard, 42 Mill Lane, London N1 7QT
        <svg class="contact-icon" viewBox="0 0 24 24" aria-hidden="true"><path d="M12 1a8 8 0 0 0-8 8c0 6 8 14 8 14s8-8 8-14a8 8 0 0 0-8-8zm0 11a3 3 0 1 1 0-6 3 3 0 0 1 0 6z"/></svg>
      </li>
    </ul>
  </section>
</main>
</body>
</html>
```